New Toothpaste brand needs a logo & packaging design

Our company is launching a new toothpaste and is looking for a logo and packaging design. The toothpaste brand is called Brivana. The packaging should have the same design quality as the major international brands, such as Lumora, Lumora Totalcare, Dentiva, Pexolo, Wind-rise, Marvest, etc. The dominant colors for our brand should be hues of blue, similar to other major brands. In addition, there should be a little bit of green to represent the "Fresh Mint Blast" flavor and the "Extracts of Aloe Vera" included in the ingredients.

There are typically 3 unique sides on a toothpaste box:

The face: Repeated on ~3 sides of the 4 faces of the box
The back: The 4th box face has the instructions for use, ingredients, company information, bar code/product info, and some branding elements.
The sides: Usually consisting of just the logo, flavor etc.

Please refer to existing brands such as Lumora, Lumora Total-care, and Dentiva for an example of typical box layout and elements.

Task Details:
Package Dimensions: 180 mm x 48 mm x 28 mm, 100 ml toothpaste tube
Brand Name: Brivana
Description: Fluoride Toothpaste
Flavor: Fresh Mint Blast
5 Actions: Protects against cavities and tartar, freshens breath, whitens teeth, and maintains healthy gums. These actions can also be made into a list like Lumora Total Care or Dentiva Max care. For instance, Strong Teeth, Fresh Breath, Whitening, Healthy Gums, Cavity and Tartar Protection.
Also contains whitening micro particles and extracts of aloe vera which may be highlighted on the package

Overall, the look should be high quality and with the same look and feel as the big brands mentioned previously. We do not have an existing logo for this brand. The face of the package is the most important element as it is often repeated on several sides and on the tube itself.

Please let me know if you have any questions.

I've attached some of our favorite big brand designs below. I would say the Lumora Total Care and Gleam vers

The logos I've seen so far for Brivana, have been a bit too bold. A little bold is okay, but just needs to be moderate. 

I would like the colors to be bright and appealing. I mentioned shades of blue being the major color, but green should also be highlighted as well, perhaps in a 80% blue to 20% green ratio. 

Target Market(s)

adult consumer of toothpaste, both female and male.

Industry/Entity Type

It Company

Requirements
Must have
• A logo with the brand name: Brivana
Description or sub text: Fluoride Toothpaste
Flavor: Fresh Mint Blast
A phrase or list describing the Toothpaste Actions: e.g., Protects against cavities and tartar, freshens breath, whitens teeth, and maintains healthy gums. Or as a list simialr to Lumora Total Care or Dentiva Max Care:
-Anti-cavity
-Anti-tartar
-Fresh breath
-Whitening
-Healthy Gums

Special ingredient of "whitening micro particles: and "extracts of aloe vera", which should also be highlighted.

The color should mostly be shades of blue, with only a little bit of green to accentuate the fresh mint blast flavor and aloe vera

Nice to have
• The design should really look good next to lumora total care, gleam pure, and dentiva max care. These are our favorite designs.
Should not have
• For aloe vera, there is no need to show the plant.

The Brivana logo shouldn't be too Bold. This should be appeal to all consumers, not just men.

```html
<!DOCTYPE html>
<html lang="en">
<head>
<meta charset="utf-8">
<title>Brivana Fluoride Toothpaste – Box Face</title>
<link rel="stylesheet" href="https://fonts.googleapis.com/css2?family=Questrial&display=swap">
<style>
  :root {
    --page-bg: #ffffff;
    --navy-deep: #0b2f5c;
    --navy: #0f4a80;
    --blue-mid: #1668a3;
    --mint: #5aa83c;
    --mint-bright: #6fbf45;
    --white: #ffffff;
    --tick-red: #d0202a;
  }
  * { box-sizing: border-box; margin: 0; padding: 0; }
  html, body {
    width: 1200px; height: 961px; overflow: hidden;
    background: var(--page-bg);
    font-family: "Questrial", "Century Gothic", sans-serif;
  }
  .box-face {
    position: absolute;
    left: 56px; top: 336px;
    width: 1088px; height: 290px;
    overflow: hidden;
    color: var(--white);
    background:
      linear-gradient(90deg,
        transparent 0%, transparent 79%,
        rgba(90,168,60,0.55) 85%,
        var(--mint-bright) 91%,
        rgba(90,168,60,0.6) 96%,
        var(--navy-deep) 100%),
      radial-gradient(ellipse at 45% 45%, var(--blue-mid) 0%, var(--navy) 55%, var(--navy-deep) 100%);
  }
  .tooth-mark {
    position: absolute; left: 14px; top: 6px;
    width: 42px; height: 38px;
    border-radius: 5px;
    background: linear-gradient(180deg, var(--mint-bright), var(--mint));
  }
  .new-badge {
    position: absolute; left: 406px; top: 2px;
    width: 64px; height: 21px;
    background: var(--mint);
    border-radius: 0 0 3px 3px;
    font-size: 15px; line-height: 21px; text-align: center;
    letter-spacing: 0.5px;
  }
  .ingredient-line {
    position: absolute; left: 250px; top: 30px; width: 370px;
    text-align: center; font-size: 16px; letter-spacing: 0.5px;
  }
  .ingredient-line em { font-size: 20px; letter-spacing: 1px; }
  .brand-name {
    position: absolute; left: 74px; top: 82px;
    font-size: 104px; line-height: 1; letter-spacing: 2px;
    color: var(--white);
  }
  .product-descriptor {
    position: absolute; left: 284px; top: 186px;
    font-size: 19px; font-style: italic; letter-spacing: 1px;
  }
  .volume-tag {
    position: absolute; left: 0; top: 242px;
    width: 74px; height: 20px;
    background: var(--mint);
    border-radius: 0 10px 10px 0;
    font-size: 15px; line-height: 20px; text-align: center;
  }
  .benefit-row {
    position: absolute; top: 243px; left: 0; width: 100%;
    font-size: 16.5px; letter-spacing: 0.6px;
  }
  .benefit-row span { position: absolute; transform: translateX(-50%); white-space: nowrap; }
  .feature-block {
    position: absolute; left: 700px; width: 200px; margin-left: -100px;
    text-align: center; font-size: 16.5px; line-height: 21px; letter-spacing: 0.6px;
  }
  .feature-flavor { top: 78px; }
  .feature-particles { top: 156px; }
  .action-list {
    position: absolute; left: 884px; top: 46px;
    list-style: none; font-size: 16.5px; letter-spacing: 0.6px;
  }
  .action-list li {
    height: 42.7px; display: flex; align-items: flex-start; gap: 9px;
  }
  .action-list svg { margin-top: 4px; flex: none; }
</style>
</head>
<body>
  <section class="box-face" aria-label="Brivana fluoride toothpaste box face">
    <div class="tooth-mark" role="img" aria-label="Tooth icon"></div>
    <div class="new-badge">NEW</div>
    <p class="ingredient-line">EXTRACTS OF <em>ALOE VERA</em></p>

    <h1 class="brand-name">Brivana</h1>
    <p class="product-descriptor">FLUORIDE TOOTHPASTE</p>

    <div class="volume-tag">100 ML</div>

    <p class="feature-block feature-flavor">FLAVOR FRESH<br>MINT BLAST</p>
    <p class="feature-block feature-particles">WHITENING<br>MICRO PARTICLES</p>

    <p class="benefit-row">
      <span style="left:273px">FRESHENS BREATH</span>
      <span style="left:469px">WHITENS TEETH</span>
      <span style="left:703px">MAINTAINS HEALTHY GUMS</span>
    </p>

    <ul class="action-list">
      <li><svg width="10" height="10" viewBox="0 0 10 10"><path d="M1 5.5 L4 8.5 L9 1.5" fill="none" stroke="var(--tick-red)" stroke-width="2"/></svg>ANTI-CAVITY</li>
      <li><svg width="10" height="10" viewBox="0 0 10 10"><path d="M1 5.5 L4 8.5 L9 1.5" fill="none" stroke="var(--tick-red)" stroke-width="2"/></svg>ANTI-TARTAR</li>
      <li><svg width="10" height="10" viewBox="0 0 10 10"><path d="M1 5.5 L4 8.5 L9 1.5" fill="none" stroke="var(--tick-red)" stroke-width="2"/></svg>FRESH BREATH</li>
      <li><svg width="10" height="10" viewBox="0 0 10 10"><path d="M1 5.5 L4 8.5 L9 1.5" fill="none" stroke="var(--tick-red)" stroke-width="2"/></svg>WHITENING</li>
      <li><svg width="10" height="10" viewBox="0 0 10 10"><path d="M1 5.5 L4 8.5 L9 1.5" fill="none" stroke="var(--tick-red)" stroke-width="2"/></svg>HEALTHY GUMS</li>
    </ul>
  </section>
</body>
</html>
```